Consulting/ Manufacturers Representative Website

I need a website for a consulting/manufacturer representative company in Texas called Harbor Ledge Advisors. We Uncover and implement the right solution, at the right time, in the right way. We consult, we train, we offer project management, we offer performance improvement, we offer value creation, we turn stagnation into growth, and we offer corporate performance improvement.
I want the design to load on desktop and mobile, I want the site to look and feel professional like a large firm, and I want the site to be a marketing tool and establish a strong online presence.

Target Market(s)

City Governments, State Governments, County Governments, US Government, Power Plants, Refineries, Chemical Plants, Industrial customers

Industry/Entity Type

Consulting

Number of Pages Required

5+ page

Requirements
Must have
• mobile and desktop compatible, professional look, must be a fast website, company email and contact capabilities, contact page, company logo on website, SEO optimized, must display different industries served: Energy, Public (Government, Not For Profit, Educational), Transportation & Logistics, Business Services.
• Show that I help customers operate in a cleaner, safer and more economical way.
Nice to have
• news letter, news feed, show that company is principles based.
Should not have
• slow site, cheap look

```html
<!DOCTYPE html>
<html lang="en">
<head>
<meta charset="utf-8">
<title>Harbor Ledge Advisors</title>
<link rel="stylesheet" href="https://fonts.googleapis.com/css2?family=Nunito+Sans:wght@400;600;700;800&family=Open+Sans:wght@400;600;700&display=swap">
<style>
:root{
  --orange:#f7872a;
  --ink:#1b1b1b;
  --body:#555555;
  --line:#cfcfcf;
  --panel:#f3f3f3;
  --white:#ffffff;
  --footer:#0b0b0b;
}
*{box-sizing:border-box;margin:0;padding:0}
html,body{width:1200px;height:3152px;overflow:hidden;background:var(--white)}
body{position:relative;font-family:"Open Sans",Arial,sans-serif;color:var(--body)}
.abs{position:absolute}

/* hero */
.hero{left:0;top:0;width:1200px;height:645px;
  background:linear-gradient(180deg,#3d5e86 0%,#7a8ea6 35%,#b79a7e 62%,#8a4e30 80%,#4a2a1e 100%)}
.brand{left:92px;top:120px;font-family:"Nunito Sans",sans-serif;font-weight:700;font-size:26px;color:var(--white);letter-spacing:1px;display:flex;align-items:center;gap:12px}
.brand-mark{width:22px;height:22px;background:var(--white)}
.topbar{right:95px;top:32px;font-size:17px;color:var(--white);display:flex;align-items:center;gap:10px}
.nav{right:95px;top:80px;display:flex;gap:42px;align-items:center;font-size:16px;font-weight:600;color:var(--white)}
.nav .active{color:var(--orange)}
.headline{left:0;top:236px;width:1200px;text-align:center;font-family:"Nunito Sans",sans-serif;font-weight:600;font-size:54px;line-height:69px;color:var(--white)}
.dots{left:562px;top:566px;display:flex;gap:4px}
.dots span{width:15px;height:15px;border-radius:50%;border:2px solid var(--white)}
.dots span.on{background:var(--white)}

/* welcome */
.welcome{left:98px;top:725px;width:602px;height:405px;border:2px solid var(--line);padding:30px 34px}
.welcome h2{font-family:"Nunito Sans",sans-serif;font-weight:800;font-size:35px;line-height:46px;color:var(--ink);margin-bottom:22px}
.welcome p{font-size:14px;line-height:26px;margin-bottom:20px;width:480px}
.btn{display:inline-block;background:var(--orange);color:var(--white);font-weight:700;font-size:15px;border-radius:24px;text-align:center}
.welcome .btn{width:130px;height:44px;line-height:44px;margin-top:8px}
.video{left:620px;top:763px;width:482px;height:327px;background:linear-gradient(180deg,#5a5a62 0%,#c77b2c 55%,#3a2a1a 100%);border:1px solid #bbb;z-index:2}
.play{left:210px;top:132px;width:60px;height:60px;border-radius:50%;background:var(--white)}

/* services */
.services{left:0;top:1215px;width:1200px;height:982px;background:var(--panel)}
.section-title{left:0;width:1200px;text-align:center;font-family:"Nunito Sans",sans-serif;font-weight:800;font-size:35px;color:var(--ink)}
.service{width:360px;text-align:center}
.service .icon{width:122px;height:122px;border-radius:50%;border:2px solid #bdbdbd;margin:0 auto 34px;display:flex;align-items:center;justify-content:center}
.service h3{font-weight:700;font-size:19px;color:var(--ink);margin-bottom:12px}
.service p{font-size:14.5px;line-height:27px;width:300px;margin:0 auto 12px}
.more{color:var(--orange);font-weight:700;font-size:15px}
.view-more{left:523px;top:2061px;width:154px;height:56px;line-height:56px;font-size:16px;border-radius:28px}

/* blog */
.card{width:320px;top:2355px}
.card .photo{width:320px;height:232px}
.card .body{position:absolute;left:18px;top:208px;width:284px;height:232px;background:var(--panel);text-align:center;padding-top:16px}
.card h4{font-weight:600;font-size:20px;color:var(--ink);margin-bottom:8px}
.meta{font-size:13.5px;color:var(--body);display:flex;justify-content:center;align-items:center;gap:6px;margin-bottom:16px}
.meta svg{fill:var(--orange)}
.card p{font-size:14px;line-height:24px;width:250px;margin:0 auto 16px}

/* footer */
.footer{left:0;top:2865px;width:1200px;height:287px;background:var(--footer);color:var(--white);text-align:center}
.socials{position:absolute;left:487px;top:60px;display:flex;gap:8px}
.socials span{width:50px;height:50px;border-radius:50%;border:2px solid var(--white);display:flex;align-items:center;justify-content:center}
.footer-info{position:absolute;left:0;top:142px;width:1200px;font-size:15px;display:flex;justify-content:center;gap:14px;align-items:center}
.footer-info svg{fill:var(--white)}
.footer-links{position:absolute;left:0;top:182px;width:1200px;font-size:15px;display:flex;justify-content:center;gap:12px}
.copyright{position:absolute;left:0;top:221px;width:1200px;font-size:15px}
</style>
</head>
<body>

<header class="abs hero" role="img" aria-label="Photo of a downtown city skyline at sunset"></header>
<div class="abs brand"><span class="brand-mark"></span>Harbor Ledge Advisors</div>
<div class="abs topbar">
  <svg width="16" height="16" viewBox="0 0 24 24" fill="var(--orange)"><path d="M6.6 10.8a15 15 0 0 0 6.6 6.6l2.2-2.2c.3-.3.7-.4 1-.2 1.1.4 2.3.6 3.6.6.6 0 1 .4 1 1V20c0 .6-.4 1-1 1A17 17 0 0 1 3 4c0-.6.4-1 1-1h3.5c.6 0 1 .4 1 1 0 1.3.2 2.5.6 3.6.1.3 0 .7-.2 1z"/></svg>
  <span>1 800 555 0142</span><span>|</span>
  <svg width="18" height="14" viewBox="0 0 24 18"><path d="M0 0h24v18H0z" fill="var(--orange)"/><path d="M2 2l10 8 10-8" stroke="#fff" stroke-width="1.5" fill="none"/></svg>
  <span>info@harborledgeadvisors.com</span>
</div>
<nav class="abs nav">
  <span class="active">HOME</span><span>ABOUT US</span><span>SERVICES</span><span>BLOG</span><span>CONTACT</span>
  <svg width="17" height="17" viewBox="0 0 24 24" fill="none" stroke="#fff" stroke-width="3"><circle cx="10" cy="10" r="7"/><path d="M15 15l7 7"/></svg>
</nav>
<h1 class="abs headline">We Uncover and implement<br>the right solution, at the right time,<br>in the right way</h1>
<div class="abs dots"><span class="on"></span><span></span><span></span><span></span></div>

<section class="abs welcome">
  <h2>WELCOME TO HARBOR<br>LEDGE ADVISORS</h2>
  <p>Nemo enim ipsam voluptatem quia voluptas sit aspernatur aut oditaut fugit, sed quia consequuntur mag.</p>
  <p>Dolores eos qui ratione voluptatem sequi nesciunt. Neque porro quisam est, qui dolorem ipsum quia dolor sit amet, consectetur, adipisci velit,sed quia non numquam eius modi tempora.</p>
  <span class="btn">READ MORE</span>
</section>
<div class="abs video" role="img" aria-label="Video still of two engineers in hard hats beside wind turbines at sunset">
  <div class="abs play"><svg width="60" height="60" viewBox="0 0 60 60"><circle cx="30" cy="30" r="26" fill="#222"/><path d="M24 18l18 12-18 12z" fill="#fff"/></svg></div>
</div>

<section class="abs services"></section>
<h2 class="abs section-title" style="top:1278px">OUR SERVICES</h2>

<div class="abs service" style="left:60px;top:1365px">
  <div class="icon"><svg width="56" height="50" viewBox="0 0 56 50" fill="none" stroke="var(--orange)" stroke-width="3.5"><path d="M6 6h30v20H18l-8 7v-7H6z"/><path d="M22 30v6h16l8 7v-7h4V16h-8"/></svg></div>
  <h3>CONSULT</h3>
  <p>Neque porro quisquam est, qui dolorem ipsum quia dolor sit amet, consectetur, adipi sci velit, sed quia non numquam</p>
  <span class="more">READ MORE</span>
</div>
<div class="abs service" style="left:420px;top:1365px">
  <div class="icon"><svg width="56" height="50" viewBox="0 0 56 50" fill="var(--orange)"><g stroke="var(--orange)" stroke-width="6"><path d="M20 12v32M4 28h32M9 17l22 22M31 17L9 39"/></g><circle cx="20" cy="28" r="12"/><circle cx="20" cy="28" r="5" fill="var(--panel)"/><circle cx="42" cy="12" r="8"/><circle cx="42" cy="12" r="3" fill="var(--panel)"/><circle cx="45" cy="38" r="6"/><circle cx="45" cy="38" r="2.5" fill="var(--panel)"/></svg></div>
  <h3>TRAIN</h3>
  <p>Neque porro quisquam est, qui dolorem ipsum quia dolor sit amet, consectetur, adipi sci velit, sed quia non numquam</p>
  <span class="more">READ MORE</span>
</div>
<div class="abs service" style="left:780px;top:1365px">
  <div class="icon"><svg width="60" height="50" viewBox="0 0 60 50" fill="var(--orange)"><circle cx="30" cy="10" r="8"/><circle cx="12" cy="16" r="6"/><circle cx="48" cy="16" r="6"/><path d="M16 46V30a14 14 0 0 1 28 0v16z"/><path d="M2 42V30a10 10 0 0 1 12-9v21z M58 42V30a10 10 0 0 0-12-9v21z"/></svg></div>
  <h3>PROJECT MANAGEMENT</h3>
  <p>Neque porro quisquam est, qui dolorem ipsum quia dolor sit amet, consectetur, adipi sci velit, sed quia non numquam</p>
  <span class="more">READ MORE</span>
</div>

<div class="abs service" style="left:60px;top:1705px">
  <div class="icon"><svg width="56" height="46" viewBox="0 0 56 46" fill="var(--orange)"><rect x="8" y="24" width="6" height="16"/><rect x="18" y="12" width="6" height="28"/><rect x="28" y="18" width="6" height="22"/><rect x="38" y="6" width="6" height="34"/><rect x="2" y="42" width="52" height="3"/><rect x="2" y="2" width="3" height="43"/></svg></div>
  <h3>PERFORMANCE IMPROVEMENT</h3>
  <p>Neque porro quisquam est, qui dolorem ipsum quia dolor sit amet, consectetur, adipi sci velit, sed quia non numquam</p>
  <span class="more">READ MORE</span>
</div>
<div class="abs service" style="left:420px;top:1705px">
  <div class="icon"><svg width="50" height="50" viewBox="0 0 50 50"><circle cx="25" cy="25" r="22" fill="var(--orange)"/><path d="M14 25l8 8 14-15" stroke="#fff" stroke-width="5" fill="none"/></svg></div>
  <h3>VALUE CREATION</h3>
  <p>Neque porro quisquam est, qui dolorem ipsum quia dolor sit amet, consectetur, adipi sci velit, sed quia non numquam</p>
  <span class="more">READ MORE</span>
</div>
<div class="abs service" style="left:780px;top:1705px">
  <div class="icon"><svg width="58" height="46" viewBox="0 0 58 46" fill="none" stroke="var(--orange)" stroke-width="3.5"><path d="M3 2v41h53"/><path d="M10 34l12-12 9 8 18-18"/><path d="M40 10h10v10"/></svg></div>
  <h3>STAGNATION INTO GROWTH</h3>
  <p>Neque porro quisquam est, qui dolorem ipsum quia dolor sit amet, consectetur, adipi sci velit, sed quia non numquam</p>
  <span class="more">READ MORE</span>
</div>
<span class="abs btn view-more">VIEW MORE</span>

<h2 class="abs section-title" style="top:2275px">LATEST BLOG</h2>

<article class="abs card" style="left:98px">
  <div class="photo" role="img" aria-label="Photo of a field technician working at yellow industrial piping" style="background:linear-gradient(135deg,#6d7b86,#c8a23a 60%,#e0b21c)"></div>
  <div class="body">
    <h4>Finibus Bonoruet Malor</h4>
    <div class="meta"><svg width="12" height="12" viewBox="0 0 12 12"><path d="M0 2h12v10H0zM1 4h10v7H1z" fill-rule="evenodd"/></svg>18/06/2018 &nbsp;|&nbsp; <svg width="11" height="12" viewBox="0 0 11 12"><circle cx="5.5" cy="3" r="3"/><path d="M0 12a5.5 5.5 0 0 1 11 0z"/></svg>Ava Lindqvist</div>
    <p>Nam libero tempore, cum soluta nobis est eligendi optio cumque nihil impedit quo minus id quod maximof</p>
    <span class="more">READ MORE</span>
  </div>
</article>
<article class="abs card" style="left:440px">
  <div class="photo" role="img" aria-label="Photo of two business professionals reviewing documents" style="background:linear-gradient(135deg,#8a9098,#3a3f48 60%,#5b6068)"></div>
  <div class="body">
    <h4>Finibus Bonoruet Malor</h4>
    <div class="meta"><svg width="12" height="12" viewBox="0 0 12 12"><path d="M0 2h12v10H0zM1 4h10v7H1z" fill-rule="evenodd"/></svg>18/06/2018 &nbsp;|&nbsp; <svg width="11" height="12" viewBox="0 0 11 12"><circle cx="5.5" cy="3" r="3"/><path d="M0 12a5.5 5.5 0 0 1 11 0z"/></svg>Ava Lindqvist</div>
    <p>Nam libero tempore, cum soluta nobis est eligendi optio cumque nihil impedit quo minus id quod maximof</p>
    <span class="more">READ MORE</span>
  </div>
</article>
<article class="abs card" style="left:782px">
  <div class="photo" role="img" aria-label="Photo of a power plant with smokestacks at dusk" style="background:linear-gradient(180deg,#3f5f9a 0%,#a88aa6 55%,#5a3b3a 100%)"></div>
  <div class="body">
    <h4>Finibus Bonoruet Malor</h4>
    <div class="meta"><svg width="12" height="12" viewBox="0 0 12 12"><path d="M0 2h12v10H0zM1 4h10v7H1z" fill-rule="evenodd"/></svg>18/06/2018 &nbsp;|&nbsp; <svg width="11" height="12" viewBox="0 0 11 12"><circle cx="5.5" cy="3" r="3"/><path d="M0 12a5.5 5.5 0 0 1 11 0z"/></svg>Ava Lindqvist</div>
    <p>Nam libero tempore, cum soluta nobis est eligendi optio cumque nihil impedit quo minus id quod maximof</p>
    <span class="more">READ MORE</span>
  </div>
</article>

<footer class="abs footer">
  <div class="socials" aria-label="Contact and sharing links">
    <span><svg width="18" height="14" viewBox="0 0 24 18"><path d="M0 0h24v18H0z" fill="#fff"/><path d="M2 2l10 8 10-8" stroke="#000" stroke-width="2" fill="none"/></svg></span>
    <span><svg width="16" height="16" viewBox="0 0 24 24" fill="#fff"><path d="M6.6 10.8a15 15 0 0 0 6.6 6.6l2.2-2.2c.3-.3.7-.4 1-.2 1.1.4 2.3.6 3.6.6.6 0 1 .4 1 1V20c0 .6-.4 1-1 1A17 17 0 0 1 3 4c0-.6.4-1 1-1h3.5c.6 0 1 .4 1 1 0 1.3.2 2.5.6 3.6.1.3 0 .7-.2 1z"/></svg></span>
    <span><svg width="18" height="18" viewBox="0 0 24 24" fill="none" stroke="#fff" stroke-width="2"><circle cx="12" cy="12" r="10"/><path d="M2 12h20M12 2c3 3 3 17 0 20M12 2c-3 3-3 17 0 20"/></svg></span>
    <span><svg width="14" height="18" viewBox="0 0 10 14" fill="#fff"><path d="M5 0a5 5 0 0 1 5 5c0 4-5 9-5 9S0 9 0 5a5 5 0 0 1 5-5zm0 3a2 2 0 1 0 0 4 2 2 0 0 0 0-4z" fill-rule="evenodd"/></svg></span>
  </div>
  <div class="footer-info">
    <svg width="10" height="14" viewBox="0 0 10 14"><path d="M5 0a5 5 0 0 1 5 5c0 4-5 9-5 9S0 9 0 5a5 5 0 0 1 5-5zm0 3a2 2 0 1 0 0 4 2 2 0 0 0 0-4z" fill-rule="evenodd"/></svg><span>Sequi nesciexas</span><span>|</span>
    <svg width="13" height="13" viewBox="0 0 24 24"><path d="M6.6 10.8a15 15 0 0 0 6.6 6.6l2.2-2.2c.3-.3.7-.4 1-.2 1.1.4 2.3.6 3.6.6.6 0 1 .4 1 1V20c0 .6-.4 1-1 1A17 17 0 0 1 3 4c0-.6.4-1 1-1h3.5c.6 0 1 .4 1 1 0 1.3.2 2.5.6 3.6.1.3 0 .7-.2 1z"/></svg><span>1 800 555 0142</span><span>|</span>
    <svg width="14" height="11" viewBox="0 0 24 18"><path d="M0 0h24v18H0z"/><path d="M2 2l10 8 10-8" stroke="#000" stroke-width="2" fill="none"/></svg><span>info@harborledgeadvisors.com</span>
  </div>
  <div class="footer-links"><span>Help</span><span>|</span><span>FAQ</span><span>|</span><span>Support</span><span>|</span><span>Sitemap</span><span>|</span><span>Terms Of Use</span><span>|</span><span>Privacy Statement</span></div>
  <p class="copyright">Copyright © 2018, Harbor Ledge Advisors. All rights reserved.</p>
</footer>

</body>
</html>
```